Flyer für Immobilienfirma
Zielgruppe
Immobilienfirma, klassisches Maklerunternehmen, Zielgruppe in erster Linie Familien.
Aufgabenstellung
Wir benötigen eine klassische Weihnachtskarte für unsere Kunden. Sehr schön wäre es, wenn unser Logo (als Datei anbei) mit auf der Karte erscheint. Es ist eine kreative, moderne, graphische Umsetzung des Themas 'Frohe Weihnachten' erwünscht, bitte eine Fotolösungen mit Weihnachtsbildern. Die Rückseite sollte inhaltlich wie im Beispiel gestaltet sein, die Schrift bitte aber passend zum Design der Vorderseite wählen. Wichtig, da die Karte am Ende über die Druckerei adresstechnisch personalisiert wird, benötigen wir am Ende noch die Schriftart.

```html
<!DOCTYPE html>
<html lang="de">
<head>
<meta charset="utf-8">
<title>Weihnachtskarte Lindauer Immobilien</title>
<link href="https://fonts.googleapis.com/css2?family=Great+Vibes&family=Questrial&display=swap" rel="stylesheet">
<style>
  :root {
    --page: #ecebe8;
    --kraft: #c7a87c;
    --pine: #2f4a2c;
    --pine-light: #5f7a4a;
    --berry: #a8322c;
    --white: #ffffff;
    --card-back: #fbfbfa;
    --ink: #222222;
    --rule: #bdbdbd;
    --logo-red: #c8241f;
  }
  * { box-sizing: border-box; margin: 0; padding: 0; }
  html, body { width: 1200px; height: 1191px; overflow: hidden; }
  body { background: var(--page); position: relative; font-family: "Questrial", sans-serif; }

  .card {
    position: absolute;
    left: 255px;
    width: 690px;
    height: 460px;
    box-shadow: 0 6px 18px rgba(0,0,0,0.18);
  }
  .card--front { top: 90px; background: var(--kraft); }
  .card--back { top: 641px; background: var(--card-back); }

  /* front */
  .front__photo {
    position: absolute;
    left: 82px; top: 44px;
    width: 508px; height: 300px;
    background:
      radial-gradient(ellipse at 30% 55%, rgba(168,50,44,0.55), transparent 40%),
      radial-gradient(ellipse at 60% 35%, var(--pine-light), transparent 55%),
      linear-gradient(135deg, #3c5a35 0%, var(--pine) 55%, #22361f 100%);
  }
  .front__title {
    position: absolute;
    left: 82px; width: 508px; top: 356px;
    text-align: center;
    font-family: "Great Vibes", cursive;
    font-weight: 400;
    font-size: 62px;
    color: var(--white);
    line-height: 1;
    white-space: nowrap;
  }
  .brand {
    position: absolute;
    display: flex; align-items: center; gap: 6px;
    font-family: "Questrial", sans-serif;
    color: var(--ink);
    line-height: 1.2;
  }
  .brand__mark { flex: none; width: 12px; height: 12px; background: var(--logo-red); }
  .front__brand { left: 600px; width: 84px; top: 290px; font-size: 11px; }

  /* back */
  .back__text {
    position: absolute;
    left: 42px; top: 40px;
    width: 320px;
    font-size: 13.5px;
    line-height: 1.32;
    color: var(--ink);
  }
  .back__greeting {
    font-family: "Great Vibes", cursive;
    font-size: 22px;
    margin-bottom: 12px;
    white-space: nowrap;
  }
  .back__text p { margin-bottom: 13px; }
  .back__sender { margin-top: 22px; }
  .back__divider {
    position: absolute;
    left: 385px; top: 60px;
    width: 1px; height: 300px;
    background: var(--rule);
  }
  .back__address {
    position: absolute;
    left: 420px; top: 120px;
    width: 230px;
  }
  .back__address span {
    display: block; height: 1px; background: var(--rule); margin-bottom: 38px;
  }
  .back__brand { left: 420px; top: 392px; font-size: 13px; }
</style>
</head>
<body>
  <section class="card card--front">
    <div class="front__photo" role="img" aria-label="Foto: geschmückter Weihnachtsbaum mit Kugeln und Holzanhänger"></div>
    <h1 class="front__title">Frohe Weihnachten</h1>
    <div class="brand front__brand"><span class="brand__mark"></span><span>Lindauer Immobilien</span></div>
  </section>

  <section class="card card--back">
    <div class="back__text">
      <div class="back__greeting">Liebe Kunden, Geschäftspartner &amp; Freunde!</div>
      <p>Wir möchten uns für Ihr entgegengebrachtes Vertrauen und die angenehme Zusammenarbeit bedanken.</p>
      <p>Genießen Sie die Weihnachtszeit mit vielen kleinen Freuden und kommen Sie gesund ins Jahr 2025.</p>
      <p>Aufgrund der aktuellen Notlage vieler Menschen möchten wir in diesem Jahr erneut mit einer Spende an den Kinderfonds der Stadt Auen versuchen, ein wenig Freude und Zuversicht zu schenken.</p>
      <p class="back__sender">Ihr Immobilienteam von</p>
      <p>Lindauer Immobilien<br>Rosengasse 7 | 91200 Auen</p>
      <p>Tel. 09100-555210<br>www.lindauer-immobilien.de</p>
    </div>
    <div class="back__divider"></div>
    <div class="back__address"><span></span><span></span><span></span></div>
    <div class="brand back__brand"><span class="brand__mark"></span><span>Lindauer Immobilien</span></div>
  </section>
</body>
</html>
```